Willowmere Spa and Beauty Ltd. (Name of business)

I need a business card designed for this new company based out of Toronto Ontario. We specialize in Eyelash Extensions, Manicures and Pedicures, body waxing, massages, laser hair removal and botox treatments. Also offer a variety of products for sale, such as skin cream serums, collagen gel, eye cream, etc. It is a safe relaxing and non-judgemental environnment. Clients are welcome to come be pampered for the half or full day. Many service packages to choose from.

Open 7days per week from 8am to 8pm.

Priscilla Dunmore
Spa Facilitator
Willowmere Spa and Beauty Ltd.
7200 Harcourt St; Suite 1400
Toronto ON K2P 9W4

OFFICE: 416.790.4100
FAX: 416.790.4101
CELL: 416.632.1987
EMAIL: priscilla.dunmore@willowmerespa.com

Target Market(s)

Target market is primarily female ranging from 16 years old to 50 years old.

Industry/Entity Type

Business

Contact Information for Business Card

Priscilla Dunmore
Spa Facilitator
7200 Harcourt St; Suite 1400
Toronto ON K2P 9W4

OFFICE: 416.790.4100
FAX: 416.790.4101
CELL: 416.632.1987

Logo Text

I dont have a logo yet. I would like it simple but sophisticated and modern.

Font styles to use
Serif

Requirements
Must have
• all pertinent details such as company name, logo, name and contact information, services that are offered, including package rates
Nice to have
• Company name and logo prominent. A card that is neat and the information such as address, phone number, fax, email, etc is not too crowded but laid out in an easy to read format.
• Possibly on the back of card - some of the services offered could be listed, as well as professional cream lotions and serums. Hours of operation etc.

```html
<!DOCTYPE html>
<html lang="en">
<head>
<meta charset="utf-8">
<title>Willowmere Spa and Beauty – Business Card</title>
<link rel="stylesheet" href="https://fonts.googleapis.com/css2?family=Marcellus&family=Fira+Sans:wght@300;400;600&display=swap">
<style>
  :root {
    --magenta: #d0005a;
    --paper: #ffffff;
    --ink: #4a4a4a;
    --canvas: #efece8;
    --serif: "Marcellus", Georgia, serif;
    --sans: "Fira Sans", Arial, sans-serif;
  }
  * { margin: 0; padding: 0; box-sizing: border-box; }
  html, body { width: 1200px; height: 1000px; overflow: hidden; }
  body { background: var(--canvas); font-family: var(--sans); position: relative; }

  .card {
    position: absolute; left: 250px; width: 700px; height: 400px;
    box-shadow: 0 8px 24px rgba(0,0,0,.18);
  }
  .card--front { top: 60px; background: var(--magenta); color: var(--paper); }
  .card--back { top: 540px; background: var(--paper); color: var(--ink); }

  /* Brand lockup */
  .brand { position: absolute; text-align: center; white-space: nowrap; }
  .brand__dot {
    display: block; width: 46px; height: 46px; border-radius: 50%;
    background: var(--paper); margin: 0 auto 12px;
  }
  .brand__name { font-family: var(--serif); font-size: 14px; letter-spacing: .3px; }
  .card--front .brand { top: 44px; left: 0; right: 0; }

  /* Holder */
  .holder { position: absolute; top: 160px; left: 0; right: 0; text-align: center; }
  .holder__name { font-family: var(--serif); font-weight: 400; font-size: 40px; line-height: 1; }
  .holder__title { font-weight: 300; font-size: 15px; letter-spacing: 6px; margin-top: 8px; }

  /* Contact */
  .contact { position: absolute; left: 70px; top: 268px; font-size: 16px; font-weight: 300; white-space: nowrap; }
  .contact__row { display: flex; align-items: center; gap: 12px; }
  .contact__row + .contact__row { margin-top: 16px; padding-left: 100px; }
  .contact b { font-weight: 600; }
  .contact .sep { margin: 0 10px; }
  .icon-badge {
    width: 30px; height: 30px; border-radius: 50%; background: var(--paper);
    display: flex; align-items: center; justify-content: center; flex: none;
  }

  /* Back */
  .card--back .brand { top: 70px; left: 30px; width: 190px; color: var(--magenta); }
  .card--back .brand__name { font-size: 13px; }
  .card--back .brand__dot { background: var(--magenta); }

  .offer { position: absolute; top: 44px; }
  .offer--services { left: 250px; }
  .offer--products { left: 500px; top: 90px; }
  .offer__heading { font-family: var(--serif); font-weight: 400; font-size: 26px; color: var(--magenta); margin-left: 4px; }
  .offer__list {
    list-style: none; border-left: 3px solid var(--magenta); padding: 4px 0 4px 14px;
    margin-top: 6px; font-weight: 300; font-size: 19px; line-height: 1.2; letter-spacing: .4px;
    white-space: nowrap;
  }
  .offer--products .offer__list { padding-bottom: 60px; }

  .hours {
    position: absolute; left: 190px; top: 298px; background: var(--magenta); color: var(--paper);
    font-weight: 600; font-size: 17px; padding: 7px 16px; white-space: nowrap;
  }
  .address {
    position: absolute; left: 170px; top: 345px; color: var(--magenta);
    font-size: 17px; display: flex; align-items: center; gap: 8px; white-space: nowrap;
  }
</style>
</head>
<body>

<section class="card card--front" aria-label="Business card front">
  <div class="brand">
    <span class="brand__dot"></span>
    <span class="brand__name">Willowmere Spa and Beauty</span>
  </div>
  <div class="holder">
    <h1 class="holder__name">Priscilla Dunmore</h1>
    <p class="holder__title">Spa Facilitator</p>
  </div>
  <div class="contact">
    <p class="contact__row">
      <span class="icon-badge"><svg width="16" height="16" viewBox="0 0 24 24"><path fill="#d0005a" d="M6.6 10.8a15 15 0 0 0 6.6 6.6l2.2-2.2a1 1 0 0 1 1-.25 11.4 11.4 0 0 0 3.6.57 1 1 0 0 1 1 1V20a1 1 0 0 1-1 1A17 17 0 0 1 3 4a1 1 0 0 1 1-1h3.5a1 1 0 0 1 1 1c0 1.25.2 2.45.57 3.57a1 1 0 0 1-.25 1z"/></svg></span>
      <span><b>Office:</b> 416.790.4100<span class="sep">|</span><b>Fax:</b> 416.790.4101<span class="sep">|</span><b>Cel:</b> 416.632.1987</span>
    </p>
    <p class="contact__row">
      <span class="icon-badge"><svg width="16" height="12" viewBox="0 0 16 12"><rect x="1" y="1" width="14" height="10" fill="none" stroke="#d0005a" stroke-width="1.6"/><path d="M1 1l7 6 7-6" fill="none" stroke="#d0005a" stroke-width="1.6"/></svg></span>
      <span>priscilla.dunmore@willowmerespa.com</span>
    </p>
  </div>
</section>

<section class="card card--back" aria-label="Business card back">
  <div class="brand">
    <span class="brand__dot"></span>
    <span class="brand__name">Willowmere Spa and Beauty</span>
  </div>

  <div class="offer offer--services">
    <h2 class="offer__heading">Services</h2>
    <ul class="offer__list">
      <li>Botox Treatments</li>
      <li>Body waxing</li>
      <li>Manicures and Pedicures</li>
      <li>Laser Hair Removal</li>
      <li>Eyelash Extensions</li>
      <li>Massages</li>
    </ul>
  </div>

  <div class="offer offer--products">
    <h2 class="offer__heading">Products</h2>
    <ul class="offer__list">
      <li>Skin Cream Serums</li>
      <li>Collagen Gel</li>
      <li>Eye Cream</li>
    </ul>
  </div>

  <p class="hours">Open 7 days per week from 8am to 8pm</p>
  <p class="address">
    <svg width="16" height="20" viewBox="0 0 16 20"><path fill="#d0005a" d="M8 0a8 8 0 0 0-8 8c0 6 8 12 8 12s8-6 8-12a8 8 0 0 0-8-8zm0 11a3 3 0 1 1 0-6 3 3 0 0 1 0 6z"/></svg>
    7200 Harcourt St; Suite 1400 Toronto ON K2P 9W4
  </p>
</section>

</body>
</html>
```